Brivora Collective Business Card Design

We need a business card design for Brivora Collective. We are a healthcare recruiting, wellness and education company. We partner with medical facilities to find quality candidates. We also offer free wellness courses.
The final design should communicate an emphasis on recruiting and wellness
The main purpose of the business card is to utilized it for networking events, give to hospitals, executives, VCs surgery centers and clinics. I want it to be sleek, clean, use of our brand colors and professional.

```html
<!DOCTYPE html>
<html lang="en">
<head>
<meta charset="utf-8">
<title>Brivora Collective Business Card</title>
<link href="https://fonts.googleapis.com/css2?family=Montserrat:wght@400;500;800&display=swap" rel="stylesheet">
<style>
  :root {
    --brand-green: #0b5e55;
    --brand-green-deep: #03564d;
    --brand-green-light: #3f8a80;
    --card-white: #f1f1f1;
    --ink: #2b2b2b;
    --rule: #3a3a3a;
    --backdrop: #d4d4d4;
  }
  * { box-sizing: border-box; margin: 0; padding: 0; }
  html, body {
    width: 1200px; height: 1200px; overflow: hidden;
    background: var(--backdrop);
    font-family: "Montserrat", sans-serif;
  }
  .canvas {
    position: relative; width: 1200px; height: 1200px;
    display: flex; flex-direction: column; align-items: center; justify-content: center; gap: 50px;
  }
  .card {
    width: 840px; height: 480px; border-radius: 28px; overflow: hidden; position: relative;
    box-shadow: 0 10px 24px rgba(0,0,0,0.18);
  }
  .card-back { background: var(--brand-green-deep); }
  .card-back .pattern-fill {
    position: absolute; inset: 0;
    background: linear-gradient(115deg, var(--brand-green-light) 0%, var(--brand-green) 45%, var(--brand-green-deep) 100%);
  }
  .card-back .back-wordmark {
    position: absolute; inset: 0; display: flex; align-items: center; justify-content: center;
    color: #ffffff; font-weight: 800; font-size: 34px; letter-spacing: 0.5px;
  }
  .card-front {
    background: var(--card-white);
    display: flex; align-items: center; padding: 0 70px 0 80px;
  }
  .front-brand {
    width: 300px; display: flex; align-items: center; gap: 14px;
  }
  .brand-square { width: 30px; height: 30px; background: var(--brand-green); border-radius: 5px; flex: none; }
  .brand-name { color: var(--brand-green); font-weight: 800; font-size: 32px; line-height: 1.1; }
  .divider { width: 2px; height: 170px; background: var(--rule); margin: 0 40px 0 30px; }
  .contact { color: var(--ink); }
  .person-name { color: var(--brand-green); font-weight: 800; font-size: 30px; }
  .person-title { font-size: 17px; margin-top: 4px; }
  .address { font-size: 17px; margin-top: 16px; line-height: 1.35; }
  .contact-list { list-style: none; margin-top: 16px; font-size: 17px; }
  .contact-list li { display: flex; align-items: center; gap: 10px; line-height: 1.6; }
  .contact-list svg { width: 16px; height: 16px; fill: var(--brand-green); flex: none; }
</style>
</head>
<body>
<main class="canvas">
  <section class="card card-back">
    <div class="pattern-fill" role="img" aria-label="Repeating brand pattern in shades of green"></div>
    <div class="back-wordmark">Brivora Collective</div>
  </section>

  <section class="card card-front">
    <div class="front-brand">
      <span class="brand-square"></span>
      <span class="brand-name">Brivora Collective</span>
    </div>
    <div class="divider"></div>
    <div class="contact">
      <h1 class="person-name">Delia Marsh</h1>
      <p class="person-title">Founder &amp; Director</p>
      <p class="address">4817 Alder Lane<br>Fairhaven Oregon 97402</p>
      <ul class="contact-list">
        <li>
          <svg viewBox="0 0 24 24" aria-hidden="true"><path d="M6.6 10.8a15 15 0 0 0 6.6 6.6l2.2-2.2c.3-.3.7-.4 1-.2 1.1.4 2.3.6 3.6.6.6 0 1 .4 1 1V20c0 .6-.4 1-1 1A17 17 0 0 1 3 4c0-.6.4-1 1-1h3.5c.6 0 1 .4 1 1 0 1.3.2 2.5.6 3.6.1.3 0 .7-.2 1z"/></svg>
          (555)-304-2719
        </li>
        <li>
          <svg viewBox="0 0 24 24" aria-hidden="true"><path d="M2 5h20v14H2z M2 5l10 8 10-8" /></svg>
          marsh@brivoracollective.com
        </li>
        <li>
          <svg viewBox="0 0 24 24" aria-hidden="true"><path d="M12 2a10 10 0 1 0 0 20 10 10 0 0 0 0-20zm6.9 6h-3a15 15 0 0 0-1.3-3.9A8 8 0 0 1 18.9 8zM12 4c.8 1.2 1.5 2.5 1.9 4h-3.8c.4-1.5 1.1-2.8 1.9-4zM4.3 14a8 8 0 0 1 0-4h3.4a16 16 0 0 0 0 4zm.8 2h3a15 15 0 0 0 1.3 3.9A8 8 0 0 1 5.1 16zm3-8h-3a8 8 0 0 1 4.3-3.9C8.8 5.3 8.4 6.6 8.1 8zM12 20c-.8-1.2-1.5-2.5-1.9-4h3.8c-.4 1.5-1.1 2.8-1.9 4zm2.3-6H9.7a14 14 0 0 1 0-4h4.6a14 14 0 0 1 0 4zm.3 5.9c.6-1.2 1-2.5 1.3-3.9h3a8 8 0 0 1-4.3 3.9zm1.7-5.9a16 16 0 0 0 0-4h3.4a8 8 0 0 1 0 4z"/></svg>
          www.brivoracollective.com
        </li>
      </ul>
    </div>
  </section>
</main>
</body>
</html>
```